Satchel & Compass needs new business card design

I need a new business card design. I'm looking for out-of-the-box design which represents the freedom of being a location independent entrepreneur.
I offer coaching, retreats and trips.
I would like to see designs with and without the photo.
Colors I use are black (#000000), green (#25A796) and brown (#D7C38C)
Website satchelandcompass.com

Target Market(s)

location independent entrepreneurs, digital nomads, people looking to swap the 9 to 5 for a lifestyle business

Industry/Entity Type

Business

Contact Information for Business Card

Petra Varga
Your Lifestyle Business Coach, Retreat & Trip Leader
http://satchelandcompass.com
hello@satchelandcompass.com
Live a life you don't need a holiday from

Font styles to use
Serif
Sans Serif

Requirements
Must have
• One side should contain only the logo. I would also consider having the "Live a life you don't need a holiday from" on that side too (depending on how it looks)
• Please show both sides on the designs.

```html
<!DOCTYPE html>
<html lang="en">
<head>
<meta charset="utf-8">
<title>Satchel &amp; Compass – Business Card</title>
<link rel="stylesheet" href="https://fonts.googleapis.com/css2?family=Open+Sans:wght@400;600;700&display=swap">
<style>
  :root {
    --ink: #1a1a1a;
    --green: #25a796;
    --brown: #d7c38c;
    --card: #ffffff;
    --stage: #ece8e1;
    --foliage-dark: #5f7a4a;
    --foliage-light: #b9c9a0;
  }
  * { box-sizing: border-box; margin: 0; padding: 0; }
  html, body { width: 1200px; height: 780px; overflow: hidden; }
  body {
    background: var(--stage);
    font-family: "Open Sans", Arial, sans-serif;
    color: var(--ink);
    display: flex;
    align-items: center;
    justify-content: center;
    gap: 40px;
  }
  .card {
    position: relative;
    width: 540px;
    height: 309px;
    border-radius: 16px;
    overflow: hidden;
    box-shadow: 0 6px 18px rgba(0,0,0,.15);
  }

  /* Front */
  .card--front { background: linear-gradient(135deg, #ffffff 40%, #f1f1f1); }
  .brand {
    position: absolute;
    right: 40px;
    top: 44px;
    text-align: right;
    font-weight: 700;
    font-size: 38px;
    line-height: 1.05;
    letter-spacing: 1px;
    text-transform: uppercase;
    color: var(--ink);
  }
  .social {
    position: absolute;
    right: 40px;
    top: 146px;
    display: flex;
    gap: 8px;
  }
  .social span {
    width: 22px; height: 22px;
    border-radius: 3px;
    background: var(--brown);
  }
  .portrait {
    position: absolute;
    left: 30px;
    top: 118px;
    width: 128px;
    height: 106px;
    border: 2px solid var(--brown);
    background: linear-gradient(135deg, #e9ecef, #cfc2b4 55%, #8a6a55);
  }
  .details {
    position: absolute;
    left: 176px;
    top: 176px;
  }
  .details__name { font-weight: 700; font-size: 19px; color: var(--ink); }
  .details__role { font-size: 12.5px; color: var(--green); margin-top: 1px; }
  .contact { list-style: none; margin-top: 14px; }
  .contact li {
    display: flex; align-items: center; gap: 8px;
    font-size: 12px; color: var(--ink); margin-bottom: 5px;
  }
  .contact svg { width: 18px; height: 18px; flex: none; }

  /* Back */
  .card--back {
    background: linear-gradient(160deg, var(--foliage-light) 0%, #8fa37a 35%, var(--foliage-dark) 70%, #7b9a5a 100%);
  }
  .scene { position: absolute; inset: 0; }
  .back-panel {
    position: absolute;
    right: 26px;
    top: 150px;
    width: 250px;
    height: 120px;
    border-radius: 10px;
    background: rgba(255,255,255,.72);
    display: flex;
    align-items: center;
    justify-content: center;
    text-align: center;
  }
  .back-panel .brand-text {
    font-weight: 700;
    font-size: 28px;
    line-height: 1.05;
    letter-spacing: 1px;
    text-transform: uppercase;
    color: var(--ink);
  }
</style>
</head>
<body>

  <section class="card card--front" aria-label="Card front">
    <div class="brand">Satchel &amp;<br>Compass</div>
    <div class="social" aria-hidden="true"><span></span><span></span><span></span></div>
    <div class="portrait" role="img" aria-label="Portrait photo of Petra Varga"></div>
    <div class="details">
      <p class="details__name">Petra Varga</p>
      <p class="details__role">Your Lifestyle Business Coach, Retreat &amp; Trip Leader</p>
      <ul class="contact">
        <li>
          <svg viewBox="0 0 18 18" aria-hidden="true">
            <rect width="18" height="18" rx="3" fill="#25a796"/>
            <circle cx="9" cy="9" r="5.5" fill="none" stroke="#fff" stroke-width="1.2"/>
            <ellipse cx="9" cy="9" rx="2.3" ry="5.5" fill="none" stroke="#fff" stroke-width="1"/>
            <line x1="3.5" y1="9" x2="14.5" y2="9" stroke="#fff" stroke-width="1"/>
          </svg>
          http://satchelandcompass.com
        </li>
        <li>
          <svg viewBox="0 0 18 18" aria-hidden="true">
            <rect width="18" height="18" rx="3" fill="#25a796"/>
            <rect x="3.5" y="5" width="11" height="8" fill="none" stroke="#fff" stroke-width="1.2"/>
            <polyline points="3.5,5 9,10 14.5,5" fill="none" stroke="#fff" stroke-width="1.2"/>
          </svg>
          hello@satchelandcompass.com
        </li>
      </ul>
    </div>
  </section>

  <section class="card card--back" aria-label="Card back">
    <div class="scene" role="img" aria-label="Outdoor photo of Petra Varga sitting on a wooden fence among trees and leafy plants, holding a small sign"></div>
    <div class="back-panel">
      <p class="brand-text">Satchel &amp;<br>Compass</p>
    </div>
  </section>

</body>
</html>
```